Business Card Design Project

beauty / make up / lashes

Industry/Entity Type

Business

Contact Information for Business Card

pink / gold / wait / black vintage classic elegant design

```html
<!DOCTYPE html>
<html lang="en">
<head>
<meta charset="utf-8">
<title>Business Card – Front and Back</title>
<link rel="stylesheet" href="https://fonts.googleapis.com/css2?family=Tinos:wght@400;700&display=swap">
<style>
  :root {
    --stage: #ebe7e4;
    --ink-black: #1c1a1c;
    --ink-black-soft: #2c282b;
    --pink: #e0157f;
    --pink-deep: #b80d63;
    --maroon: #7e0433;
    --gold-light: #ffe21a;
    --gold: #f2b90c;
    --gold-deep: #d98a06;
    --paper-text: #ffffff;
    --card-shadow: 0 18px 40px rgba(40, 20, 30, 0.28);
  }
  * { margin: 0; padding: 0; box-sizing: border-box; }
  html, body {
    width: 1200px;
    height: 1200px;
    overflow: hidden;
    background: var(--stage);
  }
  .canvas {
    position: relative;
    width: 1200px;
    height: 1200px;
    display: flex;
    flex-direction: column;
    align-items: center;
    justify-content: center;
    gap: 60px;
  }
  .card {
    position: relative;
    width: 900px;
    height: 514px;
    overflow: hidden;
    box-shadow: var(--card-shadow);
    font-family: "Tinos", "Times New Roman", serif;
    color: var(--paper-text);
  }
  .card-art {
    position: absolute;
    inset: 0;
    width: 100%;
    height: 100%;
  }
  .front .company-name {
    position: absolute;
    left: 104px;
    top: 58px;
    font-size: 54px;
    font-weight: 400;
    letter-spacing: 0.5px;
  }
  .contact-list {
    position: absolute;
    right: 48px;
    top: 262px;
    list-style: none;
    text-align: right;
    font-size: 23px;
    line-height: 1.2;
  }
  .contact-list li {
    display: flex;
    justify-content: flex-end;
    align-items: center;
    gap: 20px;
  }
  .contact-list .gap-after { margin-bottom: 22px; }
  .contact-icon {
    width: 18px;
    height: 18px;
    flex: none;
  }
  .contact-icon.blank { visibility: hidden; }
  .back .company-name {
    position: absolute;
    left: 0;
    right: 0;
    top: 150px;
    text-align: center;
    font-size: 78px;
    font-weight: 400;
    letter-spacing: 1px;
  }
</style>
</head>
<body>
<main class="canvas">

  <section class="card front">
    <svg class="card-art" viewBox="0 0 900 514" preserveAspectRatio="none">
      <defs>
        <linearGradient id="pinkField" x1="0" y1="0" x2="1" y2="1">
          <stop offset="0" stop-color="var(--pink)"/>
          <stop offset="1" stop-color="var(--pink-deep)"/>
        </linearGradient>
        <linearGradient id="goldBand" x1="0" y1="1" x2="1" y2="0">
          <stop offset="0" stop-color="var(--gold-deep)"/>
          <stop offset="0.35" stop-color="var(--gold-light)"/>
          <stop offset="0.65" stop-color="var(--gold)"/>
          <stop offset="1" stop-color="var(--gold-light)"/>
        </linearGradient>
      </defs>
      <rect class="swirl-pattern" width="900" height="514" fill="url(#pinkField)" role="img" aria-label="Pink background with a deep rose swirl flourish pattern"/>
      <path class="black-panel" d="M0 0 H900 V0 C700 60 390 210 210 514 H0 Z" fill="var(--ink-black)"/>
      <path class="black-sheen" d="M0 390 C240 300 520 150 900 0 C700 60 390 210 210 514 H0 Z" fill="var(--ink-black-soft)"/>
      <path class="gold-band" d="M210 514 C390 210 700 60 900 0 V26 C720 86 440 240 300 514 Z" fill="url(#goldBand)"/>
    </svg>

    <h1 class="company-name">company name</h1>

    <ul class="contact-list">
      <li class="gap-after">company address
        <svg class="contact-icon" viewBox="0 0 24 24"><path d="M12 2a7 7 0 0 0-7 7c0 5 7 13 7 13s7-8 7-13a7 7 0 0 0-7-7zm0 9.5A2.5 2.5 0 1 1 12 6.5a2.5 2.5 0 0 1 0 5z" fill="#fff"/></svg>
      </li>
      <li>0198 76 543
        <svg class="contact-icon" viewBox="0 0 24 24"><path d="M7 3l3 4-2 2c1 2.5 3.5 5 6 6l2-2 4 3-2 4C10 19 5 14 4 5z" fill="#fff"/></svg>
      </li>
      <li>0177 66 55 4433
        <svg class="contact-icon blank" viewBox="0 0 24 24"></svg>
      </li>
      <li>hello@lashstudio.com
        <svg class="contact-icon" viewBox="0 0 24 24"><rect x="3" y="6" width="18" height="12" fill="#fff"/><path d="M3 6l9 7 9-7" fill="none" stroke="var(--pink-deep)" stroke-width="1.6"/></svg>
      </li>
      <li>www.lashstudio.com
        <svg class="contact-icon" viewBox="0 0 24 24"><circle cx="12" cy="12" r="9" fill="#fff"/><path d="M3 12h18M12 3c-4 5-4 13 0 18M12 3c4 5 4 13 0 18" fill="none" stroke="var(--pink-deep)" stroke-width="1.4"/></svg>
      </li>
    </ul>
  </section>

  <section class="card back">
    <svg class="card-art" viewBox="0 0 900 514" preserveAspectRatio="none">
      <defs>
        <linearGradient id="pinkFieldBack" x1="0" y1="0" x2="1" y2="1">
          <stop offset="0" stop-color="var(--pink)"/>
          <stop offset="1" stop-color="var(--pink-deep)"/>
        </linearGradient>
      </defs>
      <rect class="swirl-pattern" width="900" height="514" fill="url(#pinkFieldBack)" role="img" aria-label="Pink background with a deep rose swirl flourish pattern"/>
      <rect class="name-band" x="0" y="130" width="900" height="130" fill="var(--maroon)"/>
      <path class="corner-black" d="M0 400 L0 514 L150 514 Z" fill="var(--ink-black)"/>
      <path class="corner-gold" d="M0 380 L172 514 L150 514 L0 400 Z" fill="var(--gold)"/>
    </svg>

    <h2 class="company-name">company name</h2>
  </section>

</main>
</body>
</html>
```